Cove Ridge Cardiac

Business cards for cardiology practice. eventually we will add picture (head shot) but for now just go with full color cards. Will need to use same template and design for three other providers with minor change in the designation besides name.
Looking for a design where logo stands out so as the name.
Industry/Entity Type
Business
Contact Information for Business Card
Vikram Desai, M.D.
Board Certified in Cardiovascular Disease, Interventional Cardiology & Nuclear Cardiology
812 Fernway, Suite B
Lindale, TX 77412
Telephone: (832) 617 2283
FAx: (832) 617-2284
Email: vdesai@coveridgecardiac.example
Web: www. coveridgecardiac.example
Look and feel
Each slider illustrates characteristics of the customer's brand and the style your logo design should communicate.

```html
<!DOCTYPE html>
<html lang="en">
<head>
<meta charset="utf-8">
<title>Cove Ridge Cardiac – Business Card</title>
<link rel="stylesheet" href="https://fonts.googleapis.com/css2?family=Ubuntu+Condensed&family=PT+Serif:wght@700&display=swap">
<style>
  :root {
    --backdrop: #e9e6e1;
    --card-white: #ffffff;
    --brand-red: #c01f2f;
    --band-black: #0d0d0d;
    --ink-dark: #1e1e1e;
    --text-light: #ffffff;
  }
  * { box-sizing: border-box; margin: 0; padding: 0; }
  html, body {
    width: 1200px;
    height: 1000px;
    overflow: hidden;
    background: var(--backdrop);
  }
  .canvas {
    width: 1200px;
    height: 1000px;
    display: flex;
    align-items: center;
    justify-content: center;
  }
  .card {
    width: 1000px;
    height: 572px;
    background: var(--card-white);
    position: relative;
    overflow: hidden;
    box-shadow: 0 8px 24px rgba(0,0,0,0.18);
    font-family: "Ubuntu Condensed", "Arial Narrow", sans-serif;
  }
  .brand-area {
    position: absolute;
    top: 0; left: 0;
    width: 100%;
    height: 330px;
  }
  .brand-block {
    position: absolute;
    right: 80px;
    top: 110px;
    display: flex;
    flex-direction: column;
    align-items: flex-end;
  }
  .brand-name {
    display: flex;
    align-items: center;
    gap: 16px;
    color: var(--brand-red);
    font-size: 68px;
    line-height: 1;
    letter-spacing: 1px;
    text-transform: uppercase;
  }
  .brand-mark {
    width: 30px;
    height: 30px;
    border-radius: 50%;
    background: var(--brand-red);
    flex: none;
  }
  .brand-tagline {
    margin-top: 12px;
    color: var(--ink-dark);
    font-size: 26px;
    letter-spacing: 0.5px;
  }
  .info-band {
    position: absolute;
    left: 0;
    top: 330px;
    width: 100%;
    height: 158px;
    background: var(--brand-red);
    color: var(--text-light);
    display: flex;
    justify-content: space-between;
    padding: 26px 56px 0 56px;
  }
  .provider-name {
    font-family: "PT Serif", Georgia, serif;
    font-weight: 700;
    font-size: 32px;
    line-height: 1.1;
  }
  .provider-credentials {
    font-size: 21px;
    line-height: 1.4;
    margin-top: 6px;
  }
  .practice-contact {
    font-size: 21px;
    line-height: 1.35;
    text-align: left;
  }
  .contact-band {
    position: absolute;
    left: 0;
    bottom: 0;
    width: 100%;
    height: 84px;
    background: var(--band-black);
    color: var(--text-light);
    display: flex;
    align-items: center;
    justify-content: center;
    gap: 48px;
    font-size: 24px;
    letter-spacing: 0.3px;
  }
</style>
</head>
<body>
  <main class="canvas">
    <article class="card">
      <section class="brand-area">
        <div class="brand-block">
          <div class="brand-name"><span class="brand-mark"></span>Cove Ridge Cardiac</div>
          <p class="brand-tagline">Cardiovascular Center of Excellence</p>
        </div>
      </section>

      <section class="info-band">
        <div class="provider">
          <h1 class="provider-name">Vikram Desai</h1>
          <p class="provider-credentials">M.D. Board Certified in Cardiovascular Disease,<br>Interventional Cardiology &amp; Nuclear Cardiology</p>
        </div>
        <address class="practice-contact" style="font-style: normal;">
          COVE RIDGE CARDIAC<br>
          812 Fernway, Suite B Lindale, TX 77412<br>
          Telephone: (832) 617 2283<br>
          FAx: (832) 617-2284
        </address>
      </section>

      <footer class="contact-band">
        <span class="contact-email">Email: vdesai@coveridgecardiac.example</span>
        <span class="contact-web">Web: www. coveridgecardiac.example</span>
      </footer>
    </article>
  </main>
</body>
</html>
```